New business card/stationary for a consulting company

I am looking for a clean and very professional looking business card for my consulting company as well as corresponding stationary. I am uploading our logo. I like simple and powerful for the feel. No graphics but I am open on everything else. Below is my contact information but would like the final to be in a version I can add my employees information into and print. Thank you.

Daniel Whitcombe
dan@fernlowadvisory.com
2837 North 9th Avenue, Summit Floor, Ashford Vale, Ohio 60483
www.fernlowadvisory.com

Industry/Entity Type

Consulting

Contact Information for Business Card

Daniel Whitcombe
dan@fernlowadvisory.com
www.fernlowadvisory.com

Font styles to use
Serif
Sans Serif

Requirements
Must have
• Our logo and the business card details.
Nice to have
• our website www.fernlowadvisory.com

```html
<!DOCTYPE html>
<html lang="en">
<head>
<meta charset="utf-8">
<title>Fernlow Advisory — Business Card</title>
<link rel="stylesheet" href="https://fonts.googleapis.com/css2?family=EB+Garamond:wght@400;600&family=Questrial&display=swap">
<style>
  :root {
    --backdrop: #e4e7e8;
    --navy-deep: #06065e;
    --navy-soft: #221f5f;
    --paper: #ffffff;
    --ink-light: #ffffff;
  }
  * { margin: 0; padding: 0; box-sizing: border-box; }
  html, body { width: 1200px; height: 900px; overflow: hidden; }
  body {
    background: var(--backdrop);
    display: flex;
    flex-direction: column;
    align-items: center;
    justify-content: center;
    gap: 48px;
  }
  .card {
    width: 640px;
    height: 366px;
    position: relative;
    overflow: hidden;
    box-shadow: 0 6px 18px rgba(0,0,0,0.12);
  }

  /* Brand lockup */
  .brand {
    display: flex;
    flex-direction: column;
    align-items: center;
    gap: 14px;
  }
  .brand-square {
    width: 30px;
    height: 30px;
  }
  .brand-name {
    font-family: "Questrial", sans-serif;
    font-size: 30px;
    letter-spacing: 0.09em;
    text-transform: uppercase;
    white-space: nowrap;
  }

  /* Front */
  .card-front {
    background: var(--navy-deep);
    display: flex;
    align-items: center;
    justify-content: center;
  }
  .card-front .brand-square { background: var(--ink-light); }
  .card-front .brand-name { color: var(--ink-light); }

  /* Back */
  .card-back { background: var(--paper); }
  .back-top {
    height: 166px;
    display: flex;
    align-items: center;
    justify-content: center;
  }
  .card-back .brand-square { background: var(--navy-soft); }
  .card-back .brand-name { color: var(--navy-soft); font-size: 28px; }
  .rule-thin {
    height: 6px;
    background: var(--navy-soft);
  }
  .back-bottom {
    position: absolute;
    left: 0; right: 0; bottom: 0;
    top: 180px;
    background: var(--navy-soft);
    display: flex;
    align-items: center;
    padding: 0 40px 0 56px;
    color: var(--ink-light);
    font-family: "EB Garamond", serif;
  }
  .holder-name {
    font-size: 27px;
    font-weight: 600;
    width: 250px;
    white-space: nowrap;
  }
  .divider {
    width: 1px;
    height: 70px;
    background: rgba(255,255,255,0.8);
    margin-right: 36px;
  }
  .contact {
    font-size: 14px;
    line-height: 1.35;
    list-style: none;
  }
  .contact .address { margin-bottom: 10px; }
  .contact-line {
    display: flex;
    align-items: center;
    gap: 7px;
  }
  .contact-line svg { width: 11px; height: 11px; flex: none; }
</style>
</head>
<body>

  <section class="card card-front" aria-label="Card front">
    <div class="brand">
      <span class="brand-square"></span>
      <span class="brand-name">Fernlow Advisory</span>
    </div>
  </section>

  <section class="card card-back" aria-label="Card back">
    <div class="back-top">
      <div class="brand">
        <span class="brand-square"></span>
        <span class="brand-name">Fernlow Advisory</span>
      </div>
    </div>
    <div class="rule-thin"></div>
    <div class="back-bottom">
      <p class="holder-name">Daniel Whitcombe</p>
      <span class="divider"></span>
      <ul class="contact">
        <li class="address">2837 North 9th Avenue, Summit Floor<br>Ashford Vale, Ohio 60483</li>
        <li class="contact-line">
          <svg viewBox="0 0 12 12" aria-hidden="true"><rect x="0.5" y="2" width="11" height="8" fill="none" stroke="#fff"/><path d="M0.5 2 6 7 11.5 2" fill="none" stroke="#fff"/></svg>
          dan@fernlowadvisory.com
        </li>
        <li class="contact-line">
          <svg viewBox="0 0 12 12" aria-hidden="true"><circle cx="6" cy="6" r="5.3" fill="none" stroke="#fff"/><ellipse cx="6" cy="6" rx="2.3" ry="5.3" fill="none" stroke="#fff"/><path d="M0.7 6h10.6" stroke="#fff"/></svg>
          www.fernlowadvisory.com
        </li>
      </ul>
    </div>
  </section>

</body>
</html>
```